Computer consultant website

Vexlo Software is a newly started computer consulting company. It's a small one-man company that provides mostly Android applications but also websites in collaboration with designers. I'm running this company on the side of full time university studies.

I'm in need of a website which will function as:
Primarily - I'll direct potential clients to the page so they can read about the company, what i offer and past work.
Secondarily - Making my company visible through the web and maybe getting new clients.

The final design should look modern, clean and professional.

Pages that will be in the final website are (Note that it's not the exact titles as the page will not be in english):
* About
* Services (what Vexlo offers)
* Portfolio/work
* Short news (like PlanHives "News and press")
* Contact.

Inspiration
http://www.planhive.example/design/87836
http://www.brambleorb.example/
http://www.planhive.example/design/845881
http://www.planhive.example/design/1369424 - Lighter design, however a bit cluttered.

No programming code is needed delivered at all. Focus on designing rather then coding.

If you have any questions, do not hesitate to send me a message.

Target Market(s)

Non-technical entrepreneurs and small companies.

Industry/Entity Type

University

Requirements
Must have
• Must have my company logo (see attachment).

Must in any way use both colors from my logo.

A way to logically rearrange content to fit smaller screens. I will implement this design so that it can be pleasantly viewed on mobile devices. You don't necessarily need to provide exactly how the design would look on mobile devices.

I need the following types of page designs:
* Landing page
* Content page
* Portfolio/work (with accompanying inside/clicked) page

Landing/start page must in any way include at least the information:
* Shorter version of "About Vexlo"
* At least 1 most recent portfolio/work entry
* At least 1 most recent news entry
* Services that Vexlo offers.
Nice to have
Should not have
• Testimonials or newsletter.

```html
<!DOCTYPE html>
<html lang="en">
<head>
<meta charset="utf-8">
<title>Vexlo – Web &amp; Mobile Development</title>
<link href="https://fonts.googleapis.com/css2?family=Arimo:ital,wght@0,400;0,700;1,400&family=Roboto:wght@300;400&family=Noto+Serif:ital,wght@1,700&display=swap" rel="stylesheet">
<style>
:root{
  --blue:#2a7ff0;
  --blue-deep:#1f4fb4;
  --green:#5fcc00;
  --green-dark:#3ea300;
  --ink:#333;
  --text:#555;
  --muted:#888;
  --line:#ccc;
  --page:#f3f3f3;
  --white:#fff;
  --footer-dark:#333031;
}
*{margin:0;padding:0;box-sizing:border-box}
html,body{width:1200px;height:1000px;overflow:hidden}
body{position:relative;background:var(--page);font-family:"Arimo",Arial,sans-serif;color:var(--ink)}
.abs{position:absolute}
a{color:inherit;text-decoration:none}

/* header */
.site-header{left:0;top:0;width:1200px;height:108px;background:var(--white)}
.brand{left:121px;top:20px;height:64px;display:flex;align-items:center;gap:14px}
.brand-dot{width:62px;height:62px;border-radius:50%;background:var(--blue)}
.brand-name{font-family:"Arimo",Arial,sans-serif;font-weight:700;font-size:50px;color:var(--ink);letter-spacing:-1px}
.main-nav{right:119px;top:49px;display:flex;gap:36px;font-family:"Arimo",Arial,sans-serif;font-size:17px;color:var(--ink)}
.main-nav .current{color:var(--blue)}

/* hero */
.hero{left:0;top:108px;width:1200px;height:324px;background:linear-gradient(120deg,#3a6cd0 0%,#2456bf 45%,#1d47a8 100%)}
.hero-title{left:120px;top:190px;font-family:"Noto Serif",Georgia,serif;font-style:italic;font-weight:700;font-size:42px;color:#6fd400;letter-spacing:-0.5px}
.hero-sub{left:120px;top:234px;width:308px;text-align:right;font-family:"Noto Serif",Georgia,serif;font-style:italic;font-weight:700;font-size:21px;color:#d9e8ff}
.hero-copy{left:122px;top:293px;width:307px;font-size:14px;line-height:17px;color:var(--white);text-align:justify;hyphens:auto}
.hero-devices{left:598px;top:150px;width:446px;height:256px;border-radius:10px;background:linear-gradient(180deg,#d8dbe0 0%,#a9b2c2 70%,#7f93be 100%)}

/* content */
.main-panel{left:120px;top:432px;width:708px;height:444px;background:var(--white);border-bottom:3px solid var(--line)}
.section-title{font-family:"Roboto",Arial,sans-serif;font-size:23px;font-weight:400;color:var(--ink)}
.section-title span{color:var(--blue)}
.welcome-title{left:143px;top:447px}
.welcome-copy{left:143px;top:487px;width:613px;font-size:12px;line-height:14.3px;color:var(--text);text-align:justify;letter-spacing:0.3px}
.welcome-copy p+p{margin-top:14px}
.btn-outline{left:665px;top:616px;width:91px;height:22px;border:1px solid var(--blue);color:var(--blue);font-size:13px;display:flex;align-items:center;justify-content:center;gap:5px}
.divider{left:143px;top:654px;width:614px;border-top:1px dotted var(--line)}
.projects-title{left:143px;top:668px}
.link-arrow{color:var(--blue);font-size:13px;display:flex;align-items:center;gap:5px}
.view-all{right:443px;top:677px}
.project{top:706px;width:200px}
.project-name{font-size:15px;color:var(--text);height:22px;padding-left:1px}
.project-thumb{width:200px;height:123px;border:1px solid var(--line);background:var(--white);padding:6px;box-shadow:0 8px 8px -6px rgba(0,0,0,.25)}
.project-shot{width:100%;height:100%;background:linear-gradient(180deg,#f2f4f7 0%,#f2f4f7 14%,#2f8fb7 14%,#2a7ca6 58%,#f3f3f3 58%)}
.project-shot.alt{background:linear-gradient(180deg,#f2f4f7 0%,#f2f4f7 14%,#2a6fd8 14%,#1b54b8 58%,#f3f3f3 58%)}

/* sidebar */
.sidebar{left:828px;top:432px;width:252px;height:444px;background:var(--white);border-bottom:3px solid var(--green)}
.side-head{left:828px;width:252px;height:45px;background:var(--green);border-bottom:3px solid var(--green-dark);color:var(--white);font-family:"Roboto",Arial,sans-serif;font-size:22px;padding:8px 0 0 24px}
.service-list{left:856px;top:490px;list-style:none;font-size:15px;color:var(--text)}
.service-list li{height:28px;display:flex;align-items:center;gap:11px}
.ring{width:13px;height:13px;border-radius:50%;border:3px solid var(--blue)}
.side-more{right:142px}
.news-date{left:857px;top:744px;font-size:15px;color:var(--blue)}
.news-title{left:856px;top:765px;font-size:13px;font-weight:700;color:#444;letter-spacing:0.3px}
.news-copy{left:856px;top:781px;width:212px;font-size:12px;line-height:14px;color:var(--muted)}

/* footer */
.site-footer{left:0;top:900px;width:1200px;height:57px;background:var(--white)}
.footer-nav{left:120px;top:922px;display:flex;gap:28px;font-family:"Roboto",Arial,sans-serif;font-size:13px;color:var(--text)}
.social{right:120px;top:913px;display:flex;gap:11px}
.social span{width:29px;height:29px;border-radius:50%;border:2px solid #8aa0c8}
.copyright{left:0;top:957px;width:1200px;height:43px;background:var(--footer-dark);color:var(--white);font-size:12px;display:flex;align-items:center;justify-content:center}
</style>
</head>
<body>

<header class="abs site-header">
  <div class="abs brand"><span class="brand-dot"></span><span class="brand-name">Vexlo</span></div>
  <nav class="abs main-nav">
    <a class="current" href="#">Home</a><a href="#">About</a><a href="#">Services</a><a href="#">Portfolio</a><a href="#">News</a><a href="#">Contact</a>
  </nav>
</header>

<section class="abs hero" role="img" aria-label="Blue background of tilted glass tiles"></section>
<h1 class="abs hero-title">Web &amp; Mobile</h1>
<div class="abs hero-sub">Development</div>
<p class="abs hero-copy" lang="en">Lorem ipsum dolor sit amet, consectetur adipiscing elit. Cras nulla tortor, sollicitudin id aliquam eu, bibendum vel quam. Vestibulum molestie pulvinar malesuada.</p>
<div class="abs hero-devices" role="img" aria-label="Smartphone and laptop showing the Vexlo brand"></div>

<main class="abs main-panel"></main>
<h2 class="abs section-title welcome-title">Welcome to <span>Vexlo</span></h2>
<div class="abs welcome-copy">
  <p>Lorem ipsum dolor sit amet, consectetur adipiscing elit. Curabitur ligula massa, aliquam id commodo quis, consectetur eu odio. Phasellus ac lobortis felis. Aliquam lobortis rutrum ipsum vel suscipit. Nunc auctor aliquet mi nec blandit. Maecenas nec egestas tellus. Cras dapibus mauris nec dui dapibus sollicitudin. Vestibulum eu tortor ac leo lobortis interdum. Praesent leo nisl, auctor sit amet aliquam ornare, blandit et nulla. Cras posuere quam velit, at hendrerit est. Quisque a augue sit amet eros ultricies ultricies.</p>
  <p>Lorem ipsum dolor sit amet, consectetur adipiscing elit. Curabitur ligula massa, aliquam id commodo quis, consectetur eu odio.</p>
</div>
<a class="abs btn-outline" href="#">Read More <svg width="14" height="8" viewBox="0 0 14 8"><path d="M0 4h11M8 1l4 3-4 3" stroke="currentColor" stroke-width="1.6" fill="none"/></svg></a>
<div class="abs divider"></div>
<h2 class="abs section-title projects-title">Recent <span>Projects</span></h2>
<a class="abs link-arrow view-all" href="#">View All <svg width="14" height="8" viewBox="0 0 14 8"><path d="M0 4h11M8 1l4 3-4 3" stroke="currentColor" stroke-width="1.6" fill="none"/></svg></a>

<div class="abs project" style="left:143px"><div class="project-name">Lorem ipsum dolor</div><div class="project-thumb"><div class="project-shot" role="img" aria-label="Screenshot of a client landing page"></div></div></div>
<div class="abs project" style="left:353px"><div class="project-name">Lorem ipsum dolor</div><div class="project-thumb"><div class="project-shot alt" role="img" aria-label="Screenshot of a mobile apps website"></div></div></div>
<div class="abs project" style="left:564px"><div class="project-name">Lorem ipsum dolor</div><div class="project-thumb"><div class="project-shot" role="img" aria-label="Screenshot of a client landing page"></div></div></div>

<aside class="abs sidebar"></aside>
<div class="abs side-head" style="top:432px">Our Services</div>
<ul class="abs service-list">
  <li><span class="ring"></span>Pellentesque vulputate</li>
  <li><span class="ring"></span>Nulla vulputate dolor</li>
  <li><span class="ring"></span>Nunc eget lorem</li>
  <li><span class="ring"></span>Nunc ac diam a tortor</li>
  <li><span class="ring"></span>Cras quis nisi in ligula</li>
</ul>
<a class="abs link-arrow side-more" style="top:643px" href="#">Read More <svg width="14" height="8" viewBox="0 0 14 8"><path d="M0 4h11M8 1l4 3-4 3" stroke="currentColor" stroke-width="1.6" fill="none"/></svg></a>

<div class="abs side-head" style="top:679px">Latest News</div>
<div class="abs news-date">27 February 2013</div>
<div class="abs news-title">Lorem ipsum dolor sit amet</div>
<p class="abs news-copy">Consectetur adipiscing elit. Duis vitae lectus sit amet turpis molestie tempor. Vestibulum sollicitudin.</p>
<a class="abs link-arrow side-more" style="top:840px" href="#">Read More <svg width="14" height="8" viewBox="0 0 14 8"><path d="M0 4h11M8 1l4 3-4 3" stroke="currentColor" stroke-width="1.6" fill="none"/></svg></a>

<footer class="abs site-footer"></footer>
<nav class="abs footer-nav"><a href="#">Home</a><a href="#">About</a><a href="#">Services</a><a href="#">Portfolio</a><a href="#">News</a><a href="#">Contact</a></nav>
<div class="abs social"><span></span><span></span><span></span></div>
<div class="abs copyright">Copyright © 2013 Vexlo. All Rights Reserved</div>

</body>
</html>
```